KTRWG Promotion Flyer to raise money and communicate our goals

We need a flyer that promotes our organization. We are a 501(c)3 trying to raise money for Arts, Education and Entrepreneurship in our small town.

We promote a social events that improve qualtiy of life and educate people on how to start and expand businesses. Our goal is to make downtown an active and thriving place with many things for people to do and enjoy as well as create a favorable place for business.

Target Market(s)

Wealthy donors and Organizations with cash

Industry/Entity Type

Education

Colors

Designer to choose colors to be used in the design.

Requirements
Must have
• Eye catching graphics and look very professional
• Should appeal to men and women
Nice to have
• Make use of any known psychological colors and fonts etc... that appeal to philanthropic people
Should not have
• Should not be complicated or confusing

```html
<!DOCTYPE html>
<html lang="en">
<head>
<meta charset="utf-8">
<title>KTRWG Promotion Flyer</title>
<link href="https://fonts.googleapis.com/css2?family=PT+Sans:wght@400;700&family=Playfair+Display:ital@1&display=swap" rel="stylesheet">
<style>
  :root {
    --stage: #3a3a3a;
    --green: #7cba3d;
    --pink: #e83e8c;
    --pink-border: #e5307f;
    --white: #ffffff;
    --ink: #333333;
    --sky: #dfe9ef;
    --wall: #c9b9a6;
    --grass: #5f8a3a;
    --path: #9a9690;
  }
  * { box-sizing: border-box; margin: 0; padding: 0; }
  html, body { width: 1200px; height: 1200px; overflow: hidden; }
  body { background: var(--stage); font-family: "PT Sans", sans-serif; }

  .flyer {
    position: absolute; left: 167px; top: 40px;
    width: 866px; height: 1120px; overflow: hidden;
    background: var(--white);
  }
  .hero {
    position: absolute; inset: 0;
    background: linear-gradient(180deg, var(--sky) 0%, #e6e9ea 14%, var(--wall) 24%, #bfae9b 34%, #6f8f4f 40%, var(--grass) 52%, #4e7a33 66%, var(--path) 88%, #8c8883 100%);
  }

  .brand {
    position: absolute; left: 48px; top: 4px; width: 209px; height: 146px;
    background: var(--white);
    display: flex; flex-direction: column; align-items: center; justify-content: center; gap: 6px;
  }
  .brand-row { display: flex; align-items: center; gap: 8px; }
  .brand-square { width: 22px; height: 22px; background: var(--pink); }
  .brand-name { font-size: 34px; font-weight: 700; color: var(--ink); letter-spacing: 1px; }
  .brand-sub { font-size: 9.5px; color: var(--ink); text-transform: uppercase; letter-spacing: .4px; text-align: center; }

  .diamond {
    position: absolute; top: 479px; width: 160px; height: 160px;
    transform: rotate(45deg); border-radius: 18px;
    border: 6px solid var(--pink-border); background: var(--white); padding: 5px;
    z-index: 2;
  }
  .diamond-fill { width: 100%; height: 100%; border-radius: 12px; }
  .diamond--hall { left: 104px; }
  .diamond--hall .diamond-fill { background: linear-gradient(135deg, #b9d3ea 0%, #a28f7c 50%, #7d6a55 100%); }
  .diamond--sign { left: 337px; }
  .diamond--sign .diamond-fill { background: linear-gradient(135deg, #cfdbe6 0%, #6b3e2e 50%, #9d9c86 100%); }
  .diamond--forest { left: 602px; }
  .diamond--forest .diamond-fill { background: linear-gradient(135deg, #e8d99a 0%, #8c9b5a 50%, #4f6a2e 100%); }

  .panel { position: absolute; left: 52px; width: 762px; color: var(--white); }
  .panel--goals { top: 598px; height: 317px; background: var(--green); padding: 83px 14px 0 22px; }
  .panel--appeal { top: 926px; height: 166px; background: var(--pink); padding: 12px 14px 0 22px; }

  .intro, .appeal-text { font-size: 14.6px; line-height: 17px; text-align: justify; }
  .divider {
    height: 2px; margin: 10px 30px 12px;
    background: linear-gradient(90deg, transparent, rgba(255,255,255,.9), transparent);
  }
  .goal-list { list-style: none; font-size: 14.6px; line-height: 17px; }
  .goal-list li { margin-bottom: 2px; }
  .goal-lead { font-weight: 700; font-size: 18px; }
</style>
</head>
<body>
  <main class="flyer">
    <div class="hero" role="img" aria-label="Photo of a large tan community hall with a red roof, a white gazebo, trees and lawn under a pale sky"></div>

    <div class="brand">
      <div class="brand-row">
        <span class="brand-square"></span>
        <span class="brand-name">KTRWG</span>
      </div>
      <p class="brand-sub">Cedar Hollow Small Business Association</p>
    </div>

    <div class="diamond diamond--hall"><div class="diamond-fill" role="img" aria-label="Photo of an open-sided pavilion hall under a blue sky"></div></div>
    <div class="diamond diamond--sign"><div class="diamond-fill" role="img" aria-label="Photo of a town welcome sign with a holiday greeting"></div></div>
    <div class="diamond diamond--forest"><div class="diamond-fill" role="img" aria-label="Photo of sunlight through a tall pine forest"></div></div>

    <section class="panel panel--goals">
      <p class="intro">The Cedar Hollow Small Business Association (KTRWG) is a local leader in the areas of Arts, Education and Entrepreneurship and is working diligently to promote Cedar Hollow and revitalize our downtown. When you become an KTRWG Member, you will be a part of the citywide work that the KTRWG does every day to improve the lives of citizens of Cedar Hollow:</p>
      <div class="divider"></div>
      <ul class="goal-list">
        <li><span class="goal-lead">We promote</span> Cedar Hollow Hotels, Shopping and Events that make Cedar Hollow a pleasant, exciting and prosperous place to live.</li>
        <li><span class="goal-lead">We provide</span> training and resources to anyone interested Arts, Education and Entrepreneurship.</li>
        <li><span class="goal-lead">We help</span> entrepreneur's start and grow their businesses in a tax efficient and appropriate way.</li>
        <li><span class="goal-lead">We work</span> with all levels of local government to promote our community and create a fertile environment for growth.</li>
      </ul>
    </section>

    <section class="panel panel--appeal">
      <p class="appeal-text">Every day, we look for ways to help our local businesses grow and expand, but we need you by our side. As an KTRWG Member, you can help provide training, education and support, and you can give our many businesses a chance to grow and our citizens the opportunity to experience big town amenities and events in a small town. Members' regular monthly gifts provide a consistent, reliable income stream that allows us to spend less time fundraising—and more time helping our businesses and community. Becoming an KTRWG Member is an easy, efficient and tax-deductible way to make a difference for our community all year long. Please donate today.</p>
    </section>
  </main>
</body>
</html>
```